Website Design For Ecommerce Brand That Sells Personalized Wall Decor

We need a new website for our company Copper Lantern. Our current site is functioning through wordpress/woocomerce but we are not happy with the appearance. Our products really wow people when they receive them and we need your help making our website do the same!

Number of Pages Required

4 page

```html
<!DOCTYPE html>
<html lang="en">
<head>
<meta charset="utf-8">
<title>Copper Lantern</title>
<link href="https://fonts.googleapis.com/css2?family=Heebo:wght@300;400;500;700;800&family=Roboto:wght@300;400;500;700&display=swap" rel="stylesheet">
<style>
:root{
  --green:#5e8d55;
  --green-dark:#4f7a47;
  --green-soft:#dfe8dc;
  --ink:#1d1d1d;
  --text:#333;
  --band:#f1f1f1;
  --footer:#333333;
  --white:#fff;
}
*{box-sizing:border-box;margin:0;padding:0}
html,body{width:1200px;height:2661px;overflow:hidden}
body{font-family:'Roboto',sans-serif;color:var(--text);background:var(--white);position:relative}
.abs{position:absolute}
.topbar{top:0;left:0;width:1200px;height:30px;background:var(--green);color:var(--white);font-size:13px}
.topbar .mail{position:absolute;left:163px;top:7px;display:flex;align-items:center;gap:8px}
.topbar .icons{position:absolute;right:172px;top:6px;display:flex;gap:14px}
.topbar .icons span{width:18px;height:18px;display:flex;align-items:center;justify-content:center}
.topbar .icons span+span{border-left:1px solid rgba(255,255,255,.4);padding-left:14px;width:32px}
.header{top:30px;left:0;width:1200px;height:75px;background:var(--white)}
.search{position:absolute;left:161px;top:18px;width:286px;height:38px;border:1px solid #ddd;border-radius:20px;font-size:14px;color:#999;padding:10px 20px}
.search .btn{position:absolute;right:1px;top:1px;width:34px;height:34px;border-radius:50%;background:var(--green);display:flex;align-items:center;justify-content:center}
.brand{position:absolute;left:540px;top:8px;width:120px;text-align:center;font-family:'Heebo',sans-serif;color:var(--ink);line-height:1}
.brand .mark{width:16px;height:16px;border-radius:50%;background:var(--ink);margin:0 auto 4px}
.brand .name{font-size:20px;font-weight:500;letter-spacing:1px}
.nav{position:absolute;right:162px;top:28px;display:flex;gap:34px;font-size:14px;color:var(--ink)}
.nav .active{color:var(--green)}
.hero{top:105px;left:0;width:1200px;height:470px;overflow:hidden;border-radius:0 0 50% 50%/0 0 90px 90px;background:linear-gradient(100deg,#1b1714 0%,#3a2c24 30%,#6d5446 55%,#4b362c 80%,#2a1e1a 100%)}
.hero .copy{position:absolute;left:163px;top:125px;color:var(--white)}
.hero h1{font-family:'Heebo',sans-serif;font-weight:400;font-size:40px;line-height:50px}
.hero h1 b{display:block;font-weight:700;font-size:48px}
.hero p{font-size:15px;line-height:21px;margin-top:14px;width:290px}
.btn-green{display:inline-block;background:var(--green);color:var(--white);font-weight:500;border-radius:3px}
.hero .btn-green{margin-top:20px;padding:10px 23px;font-size:14px}
.features{top:609px;left:0;width:1200px;height:104px;background:var(--band)}
.feature{position:absolute;top:21px;display:flex;align-items:center;gap:14px;font-family:'Heebo',sans-serif;font-weight:500;font-size:18px;line-height:21px;color:var(--ink)}
.feature .ico{width:62px;height:62px;border:2px solid var(--green);display:flex;align-items:center;justify-content:center}
.feature .ico .fill{width:38px;height:38px;background:var(--green-soft)}
.section-title{font-family:'Heebo',sans-serif;font-size:32px;font-weight:400;color:var(--ink);text-align:center;width:1200px;left:0}
.section-title b{font-weight:800}
.rule{width:100px;height:2px;background:var(--green);left:550px}
.tabs{top:868px;left:334px;display:flex;font-size:16px;color:var(--ink)}
.tabs span{margin-right:58px}
.tabs .on{color:var(--green);text-decoration:underline;text-underline-offset:3px}
.product{width:206px;text-align:center}
.product .img{width:206px;height:206px}
.product .title{font-size:12.5px;line-height:20px;color:var(--text);margin-top:14px;white-space:nowrap}
.product .price{font-size:16px;font-weight:700;color:var(--ink);margin-top:8px}
.promo{top:1628px;left:161px;width:878px;height:389px;box-shadow:0 0 14px rgba(0,0,0,.07);background:var(--white)}
.promo .text{position:absolute;left:0;top:0;width:439px;height:389px;text-align:center;padding-top:96px;font-family:'Heebo',sans-serif}
.promo h2{font-size:32px;font-weight:400;line-height:34px;color:var(--ink)}
.promo p{font-size:20px;font-weight:300;line-height:26px;margin-top:12px;color:var(--text)}
.promo .btn-green{margin-top:20px;padding:11px 23px;font-size:14px;border-radius:0}
.promo .pic{position:absolute;left:439px;top:0;width:439px;height:389px;background:linear-gradient(135deg,#a9b6c8 0%,#4c3a2f 45%,#3a2c24 70%,#6a8a66 100%)}
.touch-sub{top:2160px;left:0;width:1200px;text-align:center;color:var(--green);font-family:'Heebo',sans-serif;font-size:20px}
.subscribe{top:2203px;left:372px;width:456px;height:40px;display:flex;box-shadow:0 0 8px rgba(0,0,0,.1)}
.subscribe .field{flex:1;background:var(--white);border:1px solid #eee;font-size:14px;color:#888;padding:11px 14px;font-family:'Heebo',sans-serif}
.subscribe .go{width:120px;background:var(--green);color:var(--white);font-weight:700;font-size:14px;display:flex;align-items:center;justify-content:center}
.footer{top:2332px;left:0;width:1200px;height:284px;background:var(--footer);color:#e6e6e6}
.footer .logo{position:absolute;left:174px;top:70px;width:145px;text-align:center;font-family:'Heebo',sans-serif;color:var(--white)}
.footer .logo .mark{width:18px;height:18px;border-radius:50%;background:var(--white);margin:0 auto 6px}
.footer .logo .name{font-size:24px;font-weight:500;letter-spacing:1px;line-height:26px}
.footer .hr{position:absolute;left:174px;top:180px;width:145px;height:1px;background:#555}
.social{position:absolute;left:175px;top:198px;display:flex;gap:11px}
.social span{width:27px;height:27px;border:1px solid #ddd;display:flex;align-items:center;justify-content:center}
.social span i{width:7px;height:7px;background:#ddd;border-radius:50%}
.social span.on{border-color:var(--green)}
.social span.on i{background:var(--green)}
.footer h3{position:absolute;top:72px;font-family:'Heebo',sans-serif;font-weight:400;font-size:18px;color:var(--white)}
.footer h3 b{font-weight:700}
.contact{position:absolute;left:424px;top:112px;font-size:14px;line-height:21px}
.contact li{list-style:none;display:flex;gap:10px;margin-bottom:12px}
.links{position:absolute;top:112px;font-size:14px;line-height:30px;list-style:none}
.links li::before{content:"";display:inline-block;width:6px;height:6px;background:var(--green);margin-right:8px;vertical-align:2px}
.links .on{color:var(--green)}
.bottombar{top:2616px;left:0;width:1200px;height:45px;background:var(--green);color:var(--white);font-size:14px}
.bottombar .copy{position:absolute;left:163px;top:13px}
.cards{position:absolute;right:162px;top:9px;display:flex;gap:7px}
.cards span{width:42px;height:26px;background:var(--white);border-radius:3px;color:var(--green-dark);font-size:10px;font-weight:700;display:flex;align-items:center;justify-content:center}
</style>
</head>
<body>

<div class="abs topbar">
  <div class="mail">
    <svg width="15" height="12" viewBox="0 0 15 12"><rect x="0" y="0" width="15" height="12" rx="1" fill="#fff"/><path d="M1 1l6.5 5L14 1" stroke="#5e8d55" stroke-width="1.4" fill="none"/></svg>
    support@copperlantern.com
  </div>
  <div class="icons">
    <span><svg width="13" height="14" viewBox="0 0 13 14"><circle cx="6.5" cy="4" r="3.5" fill="#fff"/><path d="M0 14c0-4 3-6 6.5-6s6.5 2 6.5 6z" fill="#fff"/></svg></span>
    <span><svg width="16" height="14" viewBox="0 0 16 14"><path d="M8 14L1.5 7.5A4 4 0 018 2.5a4 4 0 016.5 5z" fill="#fff"/></svg></span>
    <span><svg width="16" height="14" viewBox="0 0 16 14"><path d="M0 1h3l2 8h9l2-6H4.5" stroke="#fff" stroke-width="1.6" fill="none"/><rect x="4.5" y="3" width="10.5" height="6" fill="#fff"/><circle cx="6" cy="12" r="1.5" fill="#fff"/><circle cx="13" cy="12" r="1.5" fill="#fff"/></svg></span>
  </div>
</div>

<header class="abs header">
  <div class="search">Search...
    <span class="btn"><svg width="14" height="14" viewBox="0 0 14 14"><circle cx="6" cy="6" r="4.3" stroke="#fff" stroke-width="2" fill="none"/><path d="M9 9l4 4" stroke="#fff" stroke-width="2"/></svg></span>
  </div>
  <div class="brand"><div class="mark"></div><div class="name">Copper Lantern</div></div>
  <nav class="nav"><span class="active">Home</span><span>Products</span><span>FAQ</span><span>Contact Us</span></nav>
</header>

<section class="abs hero">
  <div class="abs" style="inset:0" role="img" aria-label="Engraved wooden family ornament with personalised mitten tags on a wooden table"></div>
  <div class="copy">
    <h1>Welcome To<b>Copper Lantern!</b></h1>
    <p>Lorem Ipsum is simply dummy text of the printing and typesetting industry.</p>
    <span class="btn-green">Shop Now</span>
  </div>
</section>

<section class="abs features">
  <div class="feature" style="left:161px">
    <span class="ico"><svg width="38" height="26" viewBox="0 0 38 26" fill="none" stroke="#5e8d55" stroke-width="1.6"><circle cx="10" cy="7" r="4"/><circle cx="28" cy="7" r="4"/><circle cx="19" cy="11" r="4"/><path d="M2 22c0-5 4-8 8-8M36 22c0-5-4-8-8-8M10 25c0-5 4-8 9-8s9 3 9 8z"/></svg></span>
    <span>Family Owned<br>Business</span>
  </div>
  <div class="feature" style="left:472px">
    <span class="ico"><span class="fill" role="img" aria-label="Laser engraver icon"></span></span>
    <span>Personalized Hand<br>Crafted Laser Designs</span>
  </div>
  <div class="feature" style="left:791px">
    <span class="ico"><span class="fill" role="img" aria-label="Country map icon"></span></span>
    <span>Made In America<br>Products</span>
  </div>
</section>

<h2 class="abs section-title" style="top:796px">FEATURED <b>PRODUCTS</b></h2>
<div class="abs rule" style="top:843px"></div>
<div class="abs tabs"><span class="on">All</span><span>New Arrivals</span><span>Latest</span><span>Top Rated</span><span>Best Selling</span></div>

<div class="abs product" style="left:161px;top:918px"><div class="img" role="img" aria-label="Family Christmas ornament with mitten tags" style="background:linear-gradient(160deg,#2c3a2b,#a7442f 40%,#7b5a44 70%,#5c4232)"></div><div class="title">Custom Family Christmas<br>Ornament – Mitten</div><div class="price">$17.00 – $26.00</div></div>
<div class="abs product" style="left:384px;top:918px"><div class="img" role="img" aria-label="Shiplap family tree sign" style="background:linear-gradient(160deg,#eeeae6,#d8c6ac 50%,#c8b293)"></div><div class="title">Faux Shiplap Personalized<br>Family Tree</div><div class="price">$69.00</div></div>
<div class="abs product" style="left:608px;top:918px"><div class="img" role="img" aria-label="Framed family tree wall decor" style="background:linear-gradient(160deg,#5d6b58,#3e3028 45%,#c9bfb2 75%,#6f6a62)"></div><div class="title">12 Inch Square Framed Personalized<br>Family Tree Wall Decor</div><div class="price">$62.00</div></div>
<div class="abs product" style="left:832px;top:918px"><div class="img" role="img" aria-label="Pet memorial ornament" style="background:linear-gradient(160deg,#8a2a2a,#7a5a48 35%,#d9c6b4 60%,#6c5040)"></div><div class="title">In Memory of Lost<br>Pet Ornament</div><div class="price">$16.00</div></div>

<div class="abs product" style="left:161px;top:1231px"><div class="img" role="img" aria-label="Unpainted mushroom wood piece" style="background:linear-gradient(160deg,#8c7f74,#d6cab8 50%,#7d7066)"></div><div class="title">Mushroom – Interchangeable<br>Piece For Gnome Kit –<br>Unpainted</div><div class="price">$3.00</div></div>
<div class="abs product" style="left:384px;top:1231px"><div class="img" role="img" aria-label="Engraved wooden hearts" style="background:linear-gradient(160deg,#f4f1ec,#dcc29c 50%,#f1ede8)"></div><div class="title">Personalized Hearts for<br>Your Family Tree<br>&nbsp;</div><div class="price">$5.00 – $11.75</div></div>
<div class="abs product" style="left:608px;top:1231px"><div class="img" role="img" aria-label="Unpainted pumpkin wood piece" style="background:linear-gradient(160deg,#877a70,#d9cfc2 50%,#7a6d64)"></div><div class="title">Pumpkin – Interchangeable<br>Piece For Gnome Kit –<br>Unpainted</div><div class="price">$3.00</div></div>
<div class="abs product" style="left:832px;top:1231px"><div class="img" role="img" aria-label="Unpainted watermelon wood piece" style="background:linear-gradient(160deg,#857870,#d8cec2 50%,#786c63)"></div><div class="title">Watermellon – Interchangeable<br>Piece For Gnome Kit –<br>Unpainted (Copy)</div><div class="price">$3.00</div></div>

<section class="abs promo">
  <div class="text">
    <h2>PERSONALIZE THE<br>FAMILY TREE</h2>
    <p>12 Inch Square Framed Personalized<br>Family Tree Wall Decor</p>
    <span class="btn-green">SHOP NOW</span>
  </div>
  <div class="pic" role="img" aria-label="Framed family tree wall decor with greenery"></div>
</section>

<h2 class="abs section-title" style="top:2098px">GET IN <b>TOUCH</b></h2>
<div class="abs rule" style="top:2145px"></div>
<div class="abs touch-sub">Don't Miss Latest Updates &amp; Hot Deals</div>
<div class="abs subscribe"><div class="field">Email Address</div><div class="go">NOTIFY ME</div></div>

<footer class="abs footer">
  <div class="logo"><div class="mark"></div><div class="name">Copper Lantern</div></div>
  <div class="hr"></div>
  <div class="social">
    <span class="on" aria-label="Social profile"><i></i></span>
    <span aria-label="Social profile"><i></i></span>
    <span aria-label="Social profile"><i></i></span>
    <span aria-label="Social profile"><i></i></span>
  </div>
  <h3 style="left:425px">CONTACT <b>DETAILS</b></h3>
  <ul class="contact">
    <li><svg width="12" height="16" viewBox="0 0 12 16"><path d="M6 16S0 9 0 6a6 6 0 0112 0c0 3-6 10-6 10z" fill="#5e8d55"/><circle cx="6" cy="6" r="2" fill="#333"/></svg><span>Copper Lantern<br>Birch Hollow, FL 34000</span></li>
    <li><svg width="14" height="14" viewBox="0 0 14 14"><path d="M3 0l3 3-2 2c1 2 3 4 5 5l2-2 3 3-2 3C6 14 0 8 0 3z" fill="#5e8d55"/></svg><span>555-014-2290</span></li>
    <li><svg width="14" height="14" viewBox="0 0 14 14"><path d="M14 0L0 6l5 2 1 6 3-4 3 2z" fill="#5e8d55"/></svg><span>support@copperlantern.com</span></li>
  </ul>
  <h3 style="left:743px">QUICK <b>LINKS</b></h3>
  <ul class="links" style="left:743px"><li class="on">Home</li><li>Home Decor</li><li>Gnome</li><li>Personalized Gifts</li></ul>
  <ul class="links" style="left:907px"><li>Craft Supplies</li><li>Pre-Cut Shapes</li><li>Unfinished Wood</li><li>Halloween</li></ul>
</footer>

<div class="abs bottombar">
  <div class="copy">Copyright © 2022 Copper Lantern. All Rights Reserved.</div>
  <div class="cards"><span>PayNest</span><span>Orbit</span><span>Vanta</span></div>
</div>

</body>
</html>
```